Tarjetas de visita para empresa de aluminio

Empresa con mas de 40 años vendiendo perfiles de aluminio.
Somos fábrica y almacén, queremos renovar la tarjeta de presentación de nuestros comerciales dando una imgen innovadora y tecnógica mezclado con la calidez del respeto al medio ambiente.
Añado el logo de la empresa y actual cara trasera de la tarjeta de visita, el logo es el simbolo WM y la marca TRAVENIC EXTRUSION, la frase 2extrusion y lacado de aluminio" debe cambiarse por "Diseño, extrusión, lacado, anodizado y mecanizado de precisión de aluminio" o en su defecto incluir todos esos servicios que hacemos o una frase mas pegadiza.

We are an aluminium factory, we produce and stock profiles of aluminium.
we want to renew visit card of our sellers, we are looking for something that show innovation, tecnology and environment respect.
Upload our actual logo and back of visit card, logo WM and brand TRAVENIC EXTRUSION must be keept.
Text "Extrusion y lacado de aluminio" must be changed for "Diseño, extrusion, lacado, anodizado y mecanizado de precisión de aluminio" or something like that

```html
<!DOCTYPE html>
<html lang="es">
<head>
<meta charset="utf-8">
<title>Tarjeta de visita – Aluminios Veralsur</title>
<link href="https://fonts.googleapis.com/css2?family=Oswald:wght@300;400;600&family=Roboto:wght@400&display=swap" rel="stylesheet">
<style>
  :root {
    --backdrop: #ababab;
    --card: #022f66;
    --ink: #c4dcf7;
    --ink-soft: #b3cdee;
    --rule: #d6e6fa;
  }
  html, body {
    margin: 0;
    width: 1200px;
    height: 1000px;
    overflow: hidden;
    background: var(--backdrop);
  }
  .canvas {
    position: relative;
    width: 1200px;
    height: 1000px;
  }
  .card {
    position: absolute;
    left: 294px;
    width: 613px;
    height: 351px;
    border-radius: 24px;
    background: var(--card);
  }
  .card--front { top: 112px; }
  .card--back { top: 537px; }

  .person {
    position: absolute;
    right: 298px;
    top: 154px;
    text-align: right;
    color: var(--ink);
  }
  .person__name {
    font-family: "Oswald", sans-serif;
    font-weight: 600;
    font-size: 23px;
    line-height: 28px;
    letter-spacing: 0.2px;
    margin: 0;
  }
  .person__role {
    font-family: "Roboto", sans-serif;
    font-size: 17px;
    line-height: 20px;
    margin: 0;
  }
  .divider {
    position: absolute;
    left: 340px;
    top: 155px;
    width: 2px;
    height: 60px;
    background: var(--rule);
  }
  .contact {
    position: absolute;
    left: 367px;
    top: 151px;
    margin: 0;
    padding: 0;
    list-style: none;
    font-family: "Roboto", sans-serif;
    font-size: 17px;
    line-height: 22.5px;
    color: var(--ink);
  }
  .contact li {
    display: flex;
    align-items: center;
    gap: 8px;
  }
  .contact svg {
    width: 15px;
    height: 15px;
    fill: none;
    stroke: var(--ink);
    stroke-width: 1.4;
  }

  .brand {
    position: absolute;
    left: 0;
    right: 0;
    top: 70px;
    text-align: center;
    color: var(--ink);
  }
  .brand__dot {
    display: block;
    width: 110px;
    height: 110px;
    margin: 0 auto;
    border-radius: 50%;
    border: 3px solid var(--ink-soft);
    box-sizing: border-box;
  }
  .brand__name {
    font-family: "Oswald", sans-serif;
    font-weight: 400;
    font-size: 32px;
    letter-spacing: 3px;
    margin: 26px 0 0;
    line-height: 40px;
  }
  .brand__tagline {
    font-family: "Oswald", sans-serif;
    font-weight: 300;
    font-size: 14px;
    letter-spacing: 0.6px;
    margin: 12px 0 0;
    color: var(--ink-soft);
  }
</style>
</head>
<body>
<main class="canvas">
  <section class="card card--front">
    <div class="person">
      <p class="person__name">MARCOS ORTEGA LILLO</p>
      <p class="person__role">Comercial</p>
    </div>
    <div class="divider"></div>
    <ul class="contact">
      <li>
        <svg viewBox="0 0 16 16" aria-hidden="true"><path d="M4 2l2.5 3-1.5 1.5c.8 1.8 2.2 3.2 4 4L10.5 9l3 2.5-1.5 2c-5 0-10-5-10-10z" fill="currentColor" stroke="none" style="color:var(--ink)"/></svg>
        900 412 275
      </li>
      <li>
        <svg viewBox="0 0 16 16" aria-hidden="true"><rect x="1.5" y="3.5" width="13" height="9"/><path d="M1.5 3.5l6.5 5 6.5-5"/></svg>
        info@veralsur.es
      </li>
      <li>
        <svg viewBox="0 0 16 16" aria-hidden="true"><circle cx="8" cy="8" r="6.5"/><ellipse cx="8" cy="8" rx="3" ry="6.5"/><path d="M1.5 8h13M2.5 5h11M2.5 11h11"/></svg>
        www.veralsur.es
      </li>
    </ul>
  </section>

  <section class="card card--back">
    <div class="brand">
      <span class="brand__dot"></span>
      <p class="brand__name">ALUMINIOS VERALSUR</p>
      <p class="brand__tagline">MÁS DE 40 AÑOS DE EXPERIENCIA EN CARPINTERÍA DE ALUMINIO</p>
    </div>
  </section>
</main>
</body>
</html>
```